We are full service plumbing contractors that are capable of performing all of your plumbing need...

A clean, crisp website that conveys we can handle any plumbing from drain cleaning, repairs, to new construction. But emphasis on Leak detection, under-slab and underground water service leaks, repairs, and reroutes. Leak detection by acoustical, Thermal, or tracer gas , methods.Also emphasize advanced drain cleaning technologies and equipment. Don't just poke ahole in the drain blockage, Clean the pipe, with our High pressure hydrojetters, or Chain knocker drain cables that expand to the width of the pipe being cleaned.

Number of Pages Required

5+ page

Font styles to use
Sans Serif

Requirements
Should not have
• Canned photos

```html
<!DOCTYPE html>
<html lang="en">
<head>
<meta charset="utf-8">
<title>Flowline Plumbing</title>
<link href="https://fonts.googleapis.com/css2?family=Alegreya:ital,wght@0,400;0,500;1,400&family=Open+Sans:ital,wght@0,400;0,600;0,700;1,400&family=Raleway:wght@500;600;700;800&display=swap" rel="stylesheet">
<style>
:root{
  --navy:#0f2a44;
  --navy-deep:#0b2038;
  --blue:#1c5fa8;
  --sky:#1a8fd0;
  --teal:#0a83a3;
  --yellow:#f6b51e;
  --red:#d92b2b;
  --ink:#222;
  --grey:#888;
  --light:#f1f1f1;
  --footer:#13294a;
}
*{margin:0;padding:0;box-sizing:border-box}
html,body{width:672px;height:1200px;overflow:hidden;background:#fff}
body{font-family:"Open Sans",Arial,sans-serif;color:var(--ink);position:relative}
section,header,nav,footer{position:absolute;left:0;width:672px}
.abs{position:absolute}

/* top bar */
.top-bar{top:0;height:24px;background:var(--light);font-size:7px;color:#999}
.top-bar .service-area{left:78px;top:7px}
.top-bar .top-links{left:535px;top:7px;color:#444}
/* header */
.site-header{top:24px;height:40px;background:#fff}
.brand{left:86px;top:11px;display:flex;align-items:center;gap:5px;font-family:"Raleway",sans-serif;font-weight:800;font-size:14px;color:var(--blue)}
.brand .mark{width:11px;height:11px;border-radius:50%;background:var(--blue)}
.contact-chip{display:flex;align-items:center;gap:7px}
.contact-chip .label{font-size:6px;color:#666;font-weight:600;letter-spacing:.2px}
.contact-chip .value{font-size:7px;color:#444}
.contact-chip .value.big{font-size:10.5px;font-weight:700;color:#111;font-family:"Raleway",sans-serif}
/* nav */
.main-nav{top:64px;height:26px;background:linear-gradient(#14314f,var(--navy-deep))}
.main-nav ul{list-style:none;position:absolute;left:78px;top:0;display:flex;height:26px}
.main-nav li{font-family:"Raleway",sans-serif;font-weight:700;font-size:7px;color:#fff;padding:0 11px;line-height:26px;border-right:1px solid rgba(255,255,255,.12)}
.main-nav li:last-child{border:none}
.nav-cta{position:absolute;left:499px;top:0;width:98px;height:26px;background:var(--blue);color:#fff;font-family:"Raleway",sans-serif;font-weight:700;font-size:7px;text-align:center;line-height:26px}
/* hero */
.hero{top:90px;height:243px;background:linear-gradient(100deg,#0e3a6c 0%,#11508a 45%,var(--teal) 100%);color:#fff}
.offer{left:90px;top:32px;width:225px;height:41px;background:linear-gradient(90deg,#0b2747 60%,rgba(11,39,71,0));display:flex;align-items:center;gap:8px;padding-left:4px}
.offer .price{font-family:"Raleway",sans-serif;font-weight:800;font-size:34px;color:var(--yellow);line-height:1}
.offer .price sup{font-size:17px}
.offer .head{font-family:"Raleway",sans-serif;font-weight:700;font-size:15px;color:#6fc3ff;line-height:1}
.offer .sub{font-family:"Raleway",sans-serif;font-size:13px;color:#fff;line-height:1.3}
.offer .sub b{font-weight:700}
.hero-kicker{left:78px;top:86px;font-family:"Raleway",sans-serif;font-weight:700;font-size:11px}
.hero-title{left:77px;top:96px;font-family:"Raleway",sans-serif;font-weight:800;font-size:23px;letter-spacing:.2px}
.hero-list{left:78px;top:127px;list-style:none;font-family:"Raleway",sans-serif;font-weight:500;font-size:9px}
.hero-list li{display:flex;align-items:center;gap:6px;height:15px}
.btn-red{background:var(--red);color:#fff;font-family:"Raleway",sans-serif;font-weight:700;font-size:8px;text-align:center;box-shadow:0 1px 2px rgba(0,0,0,.3)}
.hero-btn{left:77px;top:184px;width:136px;height:20px;line-height:20px}
.hero-person{left:330px;top:37px;width:132px;height:206px;background:linear-gradient(180deg,rgba(255,255,255,.10),rgba(230,180,60,.35));border-radius:50px 50px 0 0}
.appointment{left:467px;top:32px;width:134px;height:197px;background:#0b3358;border:1px solid rgba(255,255,255,.15)}
.appointment svg{position:absolute;left:0;top:0}
.appointment .title{position:absolute;top:5px;width:100%;text-align:center;font-family:"Raleway",sans-serif;font-size:10.5px;color:#1b1b1b;line-height:1.2}
.appointment .title b{font-weight:800}
.field{position:absolute;left:11px;width:112px;height:15px;background:#fff;border-radius:2px;font-size:5.5px;color:#999;padding:4px 5px}
.appointment .btn-red{position:absolute;left:21px;top:165px;width:83px;height:18px;line-height:18px}
/* feature strip */
.feature-strip{top:333px;height:65px;background:linear-gradient(#fdfdfd,#dcdcdc)}
.feature{top:0;height:65px;display:flex;align-items:center;gap:10px}
.feature h3{font-family:"Raleway",sans-serif;font-weight:600;font-size:9.5px;color:#222}
.feature h3 em{font-style:normal;color:var(--red)}
.feature p{font-size:6.2px;color:#444;line-height:1.55;margin-top:3px;width:160px}
.feature p u{font-weight:700;color:#111}
.strip-divider{left:330px;top:10px;width:2px;height:50px;background:#bbb;box-shadow:1px 0 0 #fff}
/* expertise */
.expertise{top:398px;height:212px;background:#fff}
.serif{font-family:"Alegreya",Georgia,serif}
.expertise h2{left:78px;top:44px;font-size:19px;font-weight:500}
.expertise h2 span{color:var(--sky)}
.expertise .lead{left:78px;top:75px;font-size:10.5px;font-style:italic;color:#333}
.body-text{font-size:6.6px;color:#888;line-height:1.72}
.expertise .p1{left:78px;top:92px;width:214px}
.expertise .p2{left:78px;top:137px;width:214px}
.card{width:120px}
.card .photo{width:120px;height:74px;background:linear-gradient(135deg,#5f6d7c,#b8c4cf)}
.card h4{font-family:"Alegreya",Georgia,serif;font-size:10px;font-weight:500;margin-top:15px}
.card p{margin-top:4px}
.card .more{font-size:6.2px;font-weight:700;color:var(--red);margin-top:5px}
/* services */
.services{top:628px;height:271px;background:#ebebeb}
.services h2{left:78px;top:37px;font-size:16px;font-weight:500}
.services h2::after{content:"";display:inline-block;width:17px;height:2px;background:var(--sky);margin-left:6px;vertical-align:middle}
.services .intro{left:78px;top:66px;font-size:6.4px;color:#555}
.service{top:94px;width:130px;text-align:center}
.service .icon{width:52px;height:52px;border-radius:50%;background:#fff;margin:0 auto;display:flex;align-items:center;justify-content:center;box-shadow:0 1px 3px rgba(0,0,0,.08)}
.service h4{font-family:"Raleway",sans-serif;font-weight:600;font-size:7px;margin-top:13px;color:#222}
.service p{font-size:6.4px;color:#444;line-height:1.75;margin-top:6px;padding:0 10px}
.dots{left:313px;top:225px;display:flex;gap:4px}
.dots i{width:6px;height:6px;border-radius:50%;border:1px solid #bbb;background:#fff}
.dots i:first-child{background:var(--navy);border-color:var(--navy)}
/* contact bar */
.contact-bar{top:899px;height:63px;background:linear-gradient(90deg,#31404f,#3c4a58 50%,#2a3746)}
.contact-box{top:11px;width:163px;height:40px;background:#17263a;display:flex;align-items:center;color:#fff}
.contact-box .ico{width:30px;height:40px;background:#0f1c2d;display:flex;align-items:center;justify-content:center;margin-right:8px;flex:none}
.contact-box .k{font-family:"Raleway",sans-serif;font-weight:700;font-size:6.4px;color:#5fb6e8}
.contact-box .v{font-size:6.6px;margin-top:1px;white-space:nowrap}
/* footer */
.site-footer{top:962px;height:238px;background:linear-gradient(#15305a,var(--footer));color:#8d9db3}
.site-footer h5{font-family:"Raleway",sans-serif;font-weight:700;font-size:7px;color:#fff;top:34px}
.site-footer .about{left:78px;top:56px;width:162px;font-size:6.5px;line-height:1.72}
.socials{left:78px;top:124px;display:flex;gap:6px}
.socials i{width:12px;height:12px;border-radius:50%;border:1px solid #6c7c92}
.links{list-style:none;font-size:6.3px;top:56px}
.links li{height:15.6px}
.links li::before{content:"›";margin-right:5px}
.mascot{left:460px;top:16px;width:125px;height:137px;background:radial-gradient(circle at 50% 45%,#2f6cb8,rgba(19,41,74,0) 70%)}
.newsletter{left:78px;top:158px;width:519px;height:40px;border:1px solid #2a4468;background:rgba(8,22,44,.35)}
.newsletter p{position:absolute;left:13px;top:9px;font-style:italic;font-size:7.4px;color:#4fb1ea;line-height:1.45;width:200px}
.newsletter .input{position:absolute;left:226px;top:9px;width:193px;height:19px;border:1px solid #2b4568;background:#0d2240;font-size:6px;color:#9aa;padding:5px 6px}
.newsletter .btn-red{position:absolute;left:433px;top:9px;width:71px;height:19px;line-height:19px}
.copyright{left:78px;top:213px;font-size:6.3px}
.credit{left:517px;top:213px;font-size:6.3px}
.to-top{left:647px;top:202px;width:20px;height:20px;background:#0b1a2c;color:#8896aa;font-size:7px;text-align:center;line-height:20px}
</style>
</head>
<body>

<section class="top-bar">
  <span class="abs service-area">We are Serving the Entire Cedar Vale Area Including Brookhaven &amp; Millbrook</span>
  <span class="abs top-links">Carrer &nbsp;|&nbsp; Location</span>
</section>

<header class="site-header">
  <div class="abs brand"><span class="mark"></span>Flowline Plumbing</div>
  <div class="abs contact-chip" style="left:396px;top:9px">
    <svg width="20" height="16" viewBox="0 0 20 16"><rect x="1" y="2" width="18" height="12" fill="none" stroke="#1a8fd0" stroke-width="1.4"/><path d="M1 2l9 7 9-7" fill="none" stroke="#1a8fd0" stroke-width="1.4"/></svg>
    <div><div class="label">EMAIL US</div><div class="value">info@example.com</div></div>
  </div>
  <div class="abs contact-chip" style="left:503px;top:8px">
    <svg width="20" height="20" viewBox="0 0 20 20"><circle cx="10" cy="10" r="8.5" fill="none" stroke="#1a8fd0" stroke-width="1.5"/><text x="10" y="13" font-size="7" font-family="Raleway" font-weight="700" fill="#1a8fd0" text-anchor="middle">24</text></svg>
    <div><div class="label">CALL US NOW</div><div class="value big">1800 555 0142</div></div>
  </div>
</header>

<nav class="main-nav">
  <ul>
    <li>HOME</li><li>ABOUT US</li><li>SERVICES</li><li>PRICE</li><li>GALLERY</li><li>BLOG</li><li>CONTACT US</li>
  </ul>
  <div class="nav-cta">GET APPOINTMENT</div>
</nav>

<section class="hero">
  <div class="abs offer">
    <div class="price"><sup>$</sup>99</div>
    <div><div class="head">CURRENT OFFER</div><div class="sub"><b>Any Drain</b> Cleaning</div></div>
  </div>
  <div class="abs hero-kicker">WE ARE AVAILABLE FOR</div>
  <div class="abs hero-title">PLUMING SOLUTIONS</div>
  <ul class="abs hero-list">
    <li><svg width="8" height="8" viewBox="0 0 8 8"><path d="M1 4l2 2 4-5" fill="none" stroke="#f6b51e" stroke-width="1.6"/></svg>Upfront, Flat Rate Pricing</li>
    <li><svg width="8" height="8" viewBox="0 0 8 8"><path d="M1 4l2 2 4-5" fill="none" stroke="#f6b51e" stroke-width="1.6"/></svg>Never an Overtime Charge</li>
    <li><svg width="8" height="8" viewBox="0 0 8 8"><path d="M1 4l2 2 4-5" fill="none" stroke="#f6b51e" stroke-width="1.6"/></svg>Courteous, Uniformed Professionals</li>
  </ul>
  <div class="abs btn-red hero-btn">REQUEST AN APPOINTMENT</div>
  <div class="abs hero-person" role="img" aria-label="Smiling plumber in plaid shirt with tool belt holding a wrench"></div>
  <div class="abs appointment">
    <svg width="134" height="45" viewBox="0 0 134 45"><path d="M0 0H134V33L67 45 0 33Z" fill="#f6b51e"/><path d="M0 0H134V8H0Z" fill="#ffd24d"/></svg>
    <div class="title">Schedule Your<br><b>Appointment</b></div>
    <div class="field" style="top:54px">Name</div>
    <div class="field" style="top:75px">Email</div>
    <div class="field" style="top:97px">Telephone</div>
    <div class="field" style="top:119px;height:33px">Message</div>
    <div class="btn-red">SUBMIT NOW</div>
  </div>
</section>

<section class="feature-strip">
  <div class="abs feature" style="left:86px">
    <svg width="32" height="36" viewBox="0 0 32 36"><path d="M6 4c3-2 6-1 7 2l2 5c1 2 0 3-2 4l-2 1c1 4 4 8 8 10l1-2c1-2 3-2 4-1l4 3c2 2 2 4 0 6-3 3-7 3-11 0C9 27 4 19 4 11c0-3 0-5 2-7z" fill="#d92b2b"/></svg>
    <div><h3>EMERGENCY <em>PLUMBLING</em></h3><p>We're open 24/7/365 because slab leaks and burst lines don't wait. <u>Call us now.</u></p></div>
  </div>
  <div class="abs strip-divider"></div>
  <div class="abs feature" style="left:352px">
    <svg width="34" height="34" viewBox="0 0 34 34"><circle cx="17" cy="17" r="17" fill="#222"/><rect x="9" y="15" width="16" height="3" fill="#fff"/><rect x="15" y="10" width="4" height="14" fill="#fff"/><rect x="13" y="9" width="8" height="2" fill="#fff"/></svg>
    <div><h3>PLUMBING <em>MAINTENANCE</em></h3><p>Hidden leak or clogged drain? We find and hydrojet it. <u>Call Us For Fixing</u></p></div>
  </div>
</section>

<section class="expertise">
  <h2 class="abs serif">We Are Expert In<span>Plumbing</span></h2>
  <div class="abs serif lead">Leak detection, hydrojetting and everything between</div>
  <p class="abs body-text p1">We locate under-slab and underground water service leaks by acoustic, thermal and tracer gas methods, then repair or reroute the line with minimal digging and no guesswork.</p>
  <p class="abs body-text p2">Our drain cleaning goes beyond poking a hole in the blockage. High pressure hydrojetters and chain knocker cables that expand to the full width of the pipe scour it clean, so clogs stay gone. From repairs to new construction, we handle every plumbing need.</p>
  <div class="abs card" style="left:337px;top:46px">
    <div class="photo" role="img" aria-label="Plumber in hard hat working on outdoor pipes"></div>
    <h4>Commercial Plumbing</h4>
    <p class="body-text">Underground service leaks found fast, line reroutes and jetting of main drains.</p>
    <div class="more">See Services &gt;&gt;</div>
  </div>
  <div class="abs card" style="left:470px;top:46px">
    <div class="photo" role="img" aria-label="Couple repairing a kitchen faucet at home" style="background:linear-gradient(135deg,#c9b8a8,#eee6dd)"></div>
    <h4>Residential Plumbing</h4>
    <p class="body-text">Slab leak detection, faucet and fixture repairs, and full drain pipe cleaning.</p>
    <div class="more">See Services &gt;&gt;</div>
  </div>
</section>

<section class="services">
  <h2 class="abs serif">Services that we offers</h2>
  <div class="abs intro">Acoustic, thermal and tracer gas leak detection, hydrojetting and full-width drain cleaning</div>
  <div class="abs service" style="left:72px">
    <div class="icon"><svg width="22" height="26" viewBox="0 0 22 26"><rect x="6" y="2" width="10" height="22" rx="2" fill="none" stroke="#1c5fa8" stroke-width="2"/><rect x="4" y="1" width="14" height="3" fill="#1c5fa8"/><rect x="4" y="22" width="14" height="3" fill="#1c5fa8"/><path d="M9 10l4 4-4 3" fill="none" stroke="#1c5fa8" stroke-width="1.5"/></svg></div>
    <h4>SEWER REPAIR &amp; CLEANING</h4>
    <p>High pressure hydrojetters and chain knockers clean the pipe wall to wall.</p>
  </div>
  <div class="abs service" style="left:205px">
    <div class="icon"><svg width="26" height="26" viewBox="0 0 26 26"><rect x="3" y="9" width="16" height="6" rx="2" fill="#1c5fa8"/><circle cx="18" cy="12" r="4" fill="none" stroke="#1c5fa8" stroke-width="1.6"/><rect x="4" y="15" width="4" height="3" fill="#1c5fa8"/><path d="M6 20c-1 2-1 3 0 4 1-1 1-2 0-4z" fill="#1c5fa8"/></svg></div>
    <h4>FACUET &amp; LEAK REPAIRS</h4>
    <p>Under-slab and underground leaks found by acoustic, thermal or tracer gas.</p>
  </div>
  <div class="abs service" style="left:338px">
    <div class="icon"><svg width="26" height="26" viewBox="0 0 26 26"><rect x="15" y="3" width="7" height="10" fill="#1c5fa8"/><path d="M3 12h19c0 5-3 8-8 8l1 4H8l1-5c-4-1-6-4-6-7z" fill="#1c5fa8"/></svg></div>
    <h4>REMODELING SERVICE</h4>
    <p>Bathroom and kitchen remodels plus plumbing for new construction.</p>
  </div>
  <div class="abs service" style="left:472px">
    <div class="icon"><svg width="26" height="26" viewBox="0 0 26 26"><rect x="3" y="9" width="16" height="6" rx="2" fill="#1c5fa8"/><circle cx="18" cy="12" r="4" fill="none" stroke="#1c5fa8" stroke-width="1.6"/><rect x="4" y="15" width="4" height="3" fill="#1c5fa8"/><path d="M6 20c-1 2-1 3 0 4 1-1 1-2 0-4z" fill="#1c5fa8"/></svg></div>
    <h4>PLUMBING SERVICES</h4>
    <p>Water service line repairs and reroutes done with minimal digging.</p>
  </div>
  <div class="abs dots"><i></i><i></i><i></i><i></i><i></i><i></i></div>
</section>

<section class="contact-bar">
  <div class="abs contact-box" style="left:78px">
    <div class="ico"><svg width="9" height="12" viewBox="0 0 9 12"><path d="M4.5 0A4.5 4.5 0 0 0 0 4.5C0 8 4.5 12 4.5 12S9 8 9 4.5A4.5 4.5 0 0 0 4.5 0zm0 6.3a1.8 1.8 0 1 1 0-3.6 1.8 1.8 0 0 1 0 3.6z" fill="#3aa0e0"/></svg></div>
    <div><div class="k">VISIT US:</div><div class="v">18, Harbor Building, Avenue-42, Lakeport</div></div>
  </div>
  <div class="abs contact-box" style="left:255px">
    <div class="ico"><svg width="12" height="9" viewBox="0 0 12 9"><rect width="12" height="9" fill="#3aa0e0"/><path d="M0 0l6 5 6-5" fill="none" stroke="#0f1c2d" stroke-width="1"/></svg></div>
    <div><div class="k">EMAIL US:</div><div class="v">info@flowlineplumbing.com</div></div>
  </div>
  <div class="abs contact-box" style="left:433px">
    <div class="ico"><svg width="10" height="10" viewBox="0 0 10 10"><path d="M2 0l2 2.5-1 1.5c.8 1.4 1.6 2.2 3 3l1.5-1L10 8 8.5 9.8C4 9.5.5 6 .2 1.5z" fill="#3aa0e0"/></svg></div>
    <div><div class="k">24/7 EMERGENCY CALL</div><div class="v">+1800 (555) 0187</div></div>
  </div>
</section>

<footer class="site-footer">
  <h5 class="abs" style="left:78px">ABOUT US</h5>
  <p class="abs about">Full service plumbing contractors for drain cleaning, repairs and new construction, with a focus on leak detection, slab leak repair, line reroutes and hydrojetting.</p>
  <div class="abs socials"><i></i><i></i><i></i><i></i></div>
  <h5 class="abs" style="left:255px">QUICK LINKS</h5>
  <ul class="abs links" style="left:255px"><li>About US</li><li>Get Quote</li><li>Certificaton</li><li>Contact Us</li></ul>
  <h5 class="abs" style="left:344px">SERVICES</h5>
  <ul class="abs links" style="left:344px"><li>Drain Cleaning</li><li>Leak Detection</li><li>Hydrojetting</li><li>Line Reroutes</li></ul>
  <div class="abs mascot" role="img" aria-label="Cartoon plumber mascot carrying a toolbox with 24H emergency response badge"></div>
  <div class="abs newsletter">
    <p>Subscribe now and receive weekly newsletter with new tips and exciting offers or discounts.</p>
    <div class="input">Enter your mail address</div>
    <div class="btn-red">SUBSCRIBE</div>
  </div>
  <div class="abs copyright">Copyright © Flowline Plumbing 2019. All rights reserved.</div>
  <div class="abs credit">Developed by: Flowline Plumbing</div>
  <div class="abs to-top">&#708;</div>
</footer>

</body>
</html>
```